THIS IS A LATIN MUSICAL CD BUT IN ENGLISH THE TITLE WOULD BE “BEFORE THE MORNING WINDS" JUST THAT YOU K

DIGIPACK CD COVER

THIS IS THE INFO NEEDED ON THE FRONT COVER

CD TITLE "BAJO LA LLUVIA DE ABRIL"
ARTIST: ELÍAS BRON

I WOULD NEED A GREAT DESIGN TO WIN A CORONA SONORA FOR THIS MUSICAL PROJECT. I WANT A DESIGN THAT MAY CONTAIN TERMS AS HOPE, LOVE , FREEDOM , SALVATION.

I WILL ATTACH THE PRINCIPAL SONG CALL “BEFORE THE MORNING WINDS" MAYBE YOU CAN FIND INSPIRATION AND A PICTURE OF MY GUITAR.

THIS IS THE INFO NEEDED FOR THE BACK COVER , INSIDE COVERS TOO

SONGS:
1 BAJO LA LLUVIA DE ABRIL
2 CAMINO DE ARENA
3 SOÑANDO EN LA PLAYA
4 FUEGO DEL ALBA ETERNA
5 EL VIENTO
6 ALBORADA
7 LUZ SOBRE EL RÍO
8 LA BRISA SE ALEJÓ
9 CAMINO DE ARENA (DISCO)
10 CANTO SIN FIN

Hi People i will like to say thanks for be part of this project, the truth is that I do not like to be on the cover of the disc playing my guitar even though I have pictures playing in HD, I would like more a kind of art that reflects peace, hope, salvation , also could be natural landscapes that reflect the title of the album or situations in the real life where the phrase is reflected *before the morning winds*(Album Title) ,or maybe a little child with headphones and looking the sky its just a couple of ideas you can consider, the primary focus is what happens when we hear the name of God , referent to the letters i would like to see fonts more modern . Cheers!!!!! Added Tuesday, June 9, 2015

Project Deadline Extended Reason: im currently working with all of your designs on small details. Once this is done i will have a final decision.Thank you for being part of this project Sincerely,Elias Bron Added Tuesday, June 16, 2015

Target Market(s)

all people who believe in God and not

Industry/Entity Type

Religious

Font styles to use
Serif
Sans Serif
Decorative
Script

Requirements
Must have
• original design , i will like to say thanks for be part of this project, ,I would like more a kind of art that reflects peace, hope, salvation , also could be natural landscapes that reflect the title of the album or situations in the real life where the phrase is reflected BEFORE THE MORNING WINDS (GOD) , the primary focus is what happens when we hear the name of God , the market is for people who believe in God , referent to the letters i would like to see fonts more modern, however I will be here to hope see ALL your talent friends god bless you cheers
Nice to have
• natural landscapes with people that represent the concept of the album or actual scene of daily living, also modern fonts,
Should not have
• the moon, the skeleton , dead signals , dark things, satan draws, the chains and the handaxes,etc. reflect the opposite way that i want to proyect in this music i want to proyect through my music is hope, salvation, peace, and the principal objective that is WHAT HAPPEN WHEN I HEAR THE NAME OF GOD when we live in difficult situations

```html
<!DOCTYPE html>
<html lang="es">
<head>
<meta charset="utf-8">
<title>Elías Bron — Bajo la lluvia de abril</title>
<link href="https://fonts.googleapis.com/css2?family=Exo+2:wght@500;600&display=swap" rel="stylesheet">
<style>
  :root {
    --page: #ffffff;
    --ink: #ffffff;
    --grass-gold: #b8a22a;
    --grass-green: #4f8a3a;
    --grass-deep: #2f5a2c;
    --wash-red: #c4334a;
    --wash-pink: #d98ab0;
    --wash-orange: #e0842a;
    --back-top: #d9832a;
    --back-mid: #f07a1c;
    --back-low: #f5821e;
    --sand: #c8702a;
  }
  * { margin: 0; padding: 0; box-sizing: border-box; }
  html, body {
    width: 1200px; height: 1000px; overflow: hidden;
    background: var(--page);
  }
  .canvas {
    position: relative; width: 1200px; height: 1000px;
    display: flex; align-items: center; justify-content: center; gap: 60px;
    font-family: "Exo 2", "Trebuchet MS", sans-serif;
    color: var(--ink);
  }
  .panel {
    position: relative; width: 500px; height: 500px; overflow: hidden;
  }

  /* Front cover */
  .cover-art {
    position: absolute; inset: 0;
    background:
      radial-gradient(ellipse 32% 48% at 60% 48%, rgba(217,138,176,0.85), rgba(217,138,176,0) 70%),
      radial-gradient(ellipse 40% 60% at 30% 45%, rgba(196,51,74,0.8), rgba(196,51,74,0) 75%),
      linear-gradient(90deg, var(--wash-orange) 0%, var(--grass-gold) 12%, rgba(196,51,74,0.7) 35%, rgba(150,90,110,0.6) 60%, var(--grass-green) 85%, var(--grass-deep) 100%),
      var(--grass-green);
  }
  .cover-art::after {
    content: ""; position: absolute; inset: 0;
    background: linear-gradient(180deg, rgba(255,255,255,0.05) 0%, rgba(0,0,0,0) 50%, rgba(40,110,60,0.35) 100%);
  }
  .artist-name {
    position: absolute; top: 34px; left: 0; right: 0;
    text-align: center; font-weight: 600; font-size: 21px; letter-spacing: 0.28em;
  }
  .album-title {
    position: absolute; top: 318px; left: 0; right: 0;
    text-align: center; font-weight: 600; font-size: 40px; line-height: 62px;
    letter-spacing: 0.2em;
  }

  /* Back cover */
  .back {
    background: linear-gradient(180deg, var(--back-top) 0%, var(--back-mid) 55%, var(--back-low) 100%);
  }
  .shore-scene {
    position: absolute; left: 0; right: 0; bottom: 0; height: 130px;
    background: linear-gradient(180deg, rgba(200,112,42,0) 0%, rgba(200,112,42,0.55) 45%, var(--sand) 100%);
  }
  .songs-heading {
    position: absolute; top: 58px; left: 10px;
    font-weight: 600; font-size: 18px; letter-spacing: 0.22em;
  }
  .track-list {
    position: absolute; top: 136px; left: 22px; list-style: none;
    font-weight: 500; font-size: 18px; letter-spacing: 0.2em; line-height: 35px;
  }
</style>
</head>
<body>
<main class="canvas">
  <section class="panel front-cover">
    <div class="cover-art" role="img" aria-label="Photo of a young boy crouching in tall grass, washed with orange, red, pink and green colour overlays"></div>
    <p class="artist-name">ELÍAS BRON</p>
    <h1 class="album-title">BAJO LA LLUVIA<br>DE ABRIL</h1>
  </section>

  <section class="panel back">
    <div class="shore-scene" role="img" aria-label="Faint orange-tinted photo of a sandy shoreline along the bottom edge"></div>
    <h2 class="songs-heading">SONGS:</h2>
    <ol class="track-list">
      <li>1. BAJO LA LLUVIA DE ABRIL</li>
      <li>2. CAMINO DE ARENA</li>
      <li>3. SOÑANDO EN LA PLAYA</li>
      <li>4. FUEGO DEL ALBA ETERNA</li>
      <li>5. EL VIENTO</li>
      <li>6. ALBORADA</li>
      <li>7. LUZ SOBRE EL RÍO</li>
      <li>8. LA BRISA SE ALEJÓ</li>
      <li>9. CAMINO DE ARENA (DISCO)</li>
      <li>10. CANTO SIN FIN</li>
    </ol>
  </section>
</main>
</body>
</html>
```